依頼詳細

他は、色、文字等、自由にデザインしていただき結構です。

記載項目
ロゴ、マップ、ショップインフォ、メニュー一部(初回お試し 100本¥5250・2回目以降120本 ¥6300)ミレナ ¥315
サイズ
B1
ページ数
片面
希望イメージ
シンプル 複雑
単色 カラフル
暗い 明るい
日常 高級
遊び心 厳粛
未来的 伝統的
女性的 男性的
希望する色
特になし
納品ファイル
• 高解像度JPG (.jpg)
• イラストレーター形式 (.ai)
補足説明
現在制作途中ですが仮サイト
http://www.kvr-m-mnsalon.kvr-web218.example/
です。
写真画像、いくつかアップします。(使用してもしなくてもどちらでも結構です。)
ロゴ
写真は使ってもどちらでも構いませんが、店内等いくつかアップします。
写真画像アップします。

夏らしくさわやか

皆様、たくさんのご提案いただきましてありがとうございました!

またよろしくおねがいいたします。

```html
<!DOCTYPE html>
<html lang="ja">
<head>
<meta charset="utf-8">
<title>eyelash Mira ポスター</title>
<link rel="stylesheet" href="https://fonts.googleapis.com/css2?family=Noto+Serif+JP:wght@400;700;900&family=Noto+Sans+JP:wght@400;700&display=swap">
<style>
  :root {
    --yellow: #f4e01e;
    --yellow-deep: #e8cf10;
    --band: #8c7a18;
    --band-dark: #5e5010;
    --ink: #1c1a12;
    --red: #d22a1e;
    --white: #ffffff;
    --photo-warm: #d9cbb0;
    --photo-light: #f3eee4;
    --map-light: #fbf7e4;
  }
  html, body { margin: 0; padding: 0; overflow: hidden; background: #ffffff; }
  .poster {
    position: relative; width: 843px; height: 1200px; overflow: hidden;
    background: radial-gradient(ellipse at 30% 40%, var(--yellow) 0%, var(--yellow) 55%, var(--yellow-deep) 100%);
    font-family: "Noto Sans JP", sans-serif; color: var(--ink);
  }
  .headline { margin: 0; font-family: "Noto Serif JP", serif; font-weight: 900; line-height: 1; }
  .headline span { position: absolute; white-space: nowrap; }
  .headline .first { right: 16px; top: 4px; font-size: 122px; letter-spacing: 2px; }
  .headline .second { left: 572px; top: 120px; font-size: 96px; }
  .tagline {
    position: absolute; left: 52px; top: 180px; margin: 0;
    font-family: "Noto Serif JP", serif; font-weight: 700; font-size: 27px; letter-spacing: 1px;
  }
  .eye-band {
    position: absolute; left: 0; top: 228px; width: 843px; height: 64px;
    background: linear-gradient(90deg, var(--yellow-deep), var(--band) 40%, var(--band-dark) 100%);
  }
  .eye-art {
    position: absolute; left: 336px; top: 228px; width: 507px; height: 64px;
    background: radial-gradient(ellipse at 30% 60%, rgba(40,34,8,.5), rgba(140,122,24,0) 55%),
                radial-gradient(ellipse at 82% 60%, rgba(40,34,8,.45), rgba(140,122,24,0) 50%);
  }
  .eye-caption {
    position: absolute; left: 604px; top: 234px; margin: 0;
    font-family: "Noto Serif JP", serif; font-size: 12px; line-height: 1.3; color: var(--white);
  }
  .access {
    position: absolute; left: 416px; top: 298px; margin: 0;
    font-family: "Noto Serif JP", serif; font-weight: 700; font-size: 30px; color: var(--ink);
    letter-spacing: 1px;
  }
  .offer {
    position: absolute; left: 24px; top: 356px; width: 250px; height: 150px; box-sizing: border-box;
    background: var(--white); border: 3px solid var(--red); color: var(--red);
    font-family: "Noto Serif JP", serif; font-weight: 700;
  }
  .offer-label {
    position: absolute; left: 8px; top: 6px; padding: 1px 8px;
    background: var(--red); color: var(--white); font-size: 22px;
  }
  .offer-list { position: absolute; left: 10px; top: 44px; margin: 0; padding: 0; list-style: none; }
  .offer-list li { font-size: 31px; line-height: 1.1; }
  .offer-list .sub { font-size: 17px; line-height: 1.3; }
  .intro {
    position: absolute; left: 310px; top: 350px; width: 506px; margin: 0;
    font-size: 14.5px; line-height: 1.85; color: var(--ink);
  }
  .interior-photo {
    position: absolute; left: 24px; top: 630px; width: 256px; height: 270px;
    background: linear-gradient(160deg, var(--photo-light) 0%, var(--photo-warm) 100%);
  }
  .shop-info { position: absolute; left: 440px; top: 628px; width: 380px; }
  .shop-name { margin: 0 0 6px; font-family: "Noto Serif JP", serif; font-weight: 700; font-size: 36px; }
  .shop-info p { margin: 0; font-size: 15px; line-height: 1.55; }
  .shop-info .tel { margin-top: 6px; font-size: 16px; }
  .shop-info .tel strong { font-size: 30px; font-family: "Noto Serif JP", serif; margin-left: 8px; }
  .shop-info .hours-head { margin-top: 10px; text-align: right; }
  .shop-info .hours { text-align: right; font-family: "Noto Serif JP", serif; font-weight: 700; font-size: 30px; line-height: 1.2; }
  .hours small { font-size: 14px; font-family: "Noto Sans JP", sans-serif; font-weight: 400; }
  .holiday { text-align: right; }
  .logo-badge {
    position: absolute; left: 282px; top: 936px; width: 266px; height: 156px;
    background: var(--white); border-radius: 50%;
    display: flex; align-items: center; justify-content: center;
    font-family: "Noto Serif JP", serif; font-size: 36px; color: var(--ink);
  }
  .map-area {
    position: absolute; left: 562px; top: 950px; width: 254px; height: 184px;
    background: linear-gradient(180deg, var(--map-light), #ece6c8);
    border: 1px solid rgba(0,0,0,.15);
  }
</style>
</head>
<body>
<main class="poster">
  <h1 class="headline"><span class="first">まつ毛の</span><span class="second">力。</span></h1>
  <p class="tagline">まつげエクステ専門サロン</p>

  <div class="eye-band"></div>
  <div class="eye-art" role="img" aria-label="女性の目元のイラスト"></div>
  <p class="eye-caption">eyelash Mira<br>for<br>Beauty&amp;Health</p>
  <p class="access">若葉駅東口徒歩3分</p>

  <section class="offer">
    <span class="offer-label">初回お試し</span>
    <ul class="offer-list">
      <li>100本 ¥5250</li>
      <li class="sub">(2回目以降120本 ¥6300)</li>
      <li>ミレナ ¥315</li>
    </ul>
  </section>

  <p class="intro">
    今やまつげエクステは女性の毎日に欠かせない存在です。<br>
    一本一本ていねいに、自然で美しい目元をつくります。<br>
    朝のメイク時間が短くなり、素顔にも自信が持てます。<br>
    当店では肌にやさしい素材だけを厳選して使用しています。<br>
    経験豊富なスタッフが、なりたい目元をご提案します。<br>
    落ち着いた個室で、ゆったりお過ごしいただけます。<br>
    はじめての方にもわかりやすくご説明いたします。<br>
    お仕事帰りにも通いやすい駅近のサロンです。<br>
    皆さまのご来店を心よりお待ちしております。
  </p>

  <div class="interior-photo" role="img" aria-label="サロン店内の施術スペースの写真"></div>

  <section class="shop-info">
    <h2 class="shop-name">eyelash Mira</h2>
    <p>〒100-0000 東京都みどり区若葉1-2-3 1F</p>
    <p>最寄駅 みどり線<br>若葉駅東口下車 徒歩3分</p>
    <p class="tel">TEL&amp;FAX<strong>03-5550-1247</strong></p>
    <p class="hours-head">営業時間</p>
    <p class="hours">10:00~19:00<small>(最終受付 18:30)</small></p>
    <p class="holiday">火曜日、偶数月の第3月曜日<br>(12月を除く)</p>
  </section>

  <div class="logo-badge">Mira eyelash</div>
  <div class="map-area" role="img" aria-label="若葉駅東口からサロンまでの地図"></div>
</main>
</body>
</html>
```